Talemoor

I need a webiste built to sell digital downloads. I will be selling audio books. I will be selling them by the book and also by the chapter. I already have logos (attached) and some examples of covers. I'd like it simple. I was thinking a banner with a "featured" product which scrolls between three of four and a list of products below. Clicking on one of the covers will then go to a purchase page, which will include an option to but the entire title or chapter. I want something similar to the korvath ONE website in theme and design. In terms of tabs, I will need ABOUT, TRUE CRIME, SPORT, MUSIC, AUTHORS.

```html
<!DOCTYPE html>
<html lang="en">
<head>
<meta charset="utf-8">
<title>Talemoor – Audio Books</title>
<link rel="stylesheet" href="https://fonts.googleapis.com/css2?family=Montserrat:wght@400;500&family=Playfair+Display:wght@600;700&display=swap">
<style>
:root{
  --ink:#ffffff;
  --night:#0b0c11;
  --slate:#2b3148;
  --slate-light:#323950;
  --button:#2a3046;
  --brand:#7ccf3a;
  --dot-off:#2b3148;
}
*{box-sizing:border-box;margin:0;padding:0}
html,body{width:956px;height:1200px;overflow:hidden}
body{position:relative;background:var(--slate);color:var(--ink);font-family:"Montserrat",sans-serif}
.serif{font-family:"Playfair Display",serif}
.brand{display:flex;align-items:center;gap:8px;position:absolute}
.brand-dot{width:22px;height:22px;border-radius:50%;background:var(--brand)}
.brand-name{font-family:"Montserrat",sans-serif;font-weight:500;font-size:20px;color:var(--brand)}
.site-header{position:absolute;left:0;top:0;width:956px;height:70px;background:linear-gradient(180deg,#050608 0%,#1c2030 100%);z-index:2}
.site-header .brand{left:92px;top:23px}
.nav{position:absolute;display:flex;align-items:center;font-size:15px}
.nav-item{display:flex;align-items:center;gap:10px;color:var(--ink);text-decoration:none;position:absolute;white-space:nowrap}
.nav-item svg{width:17px;height:17px;fill:var(--ink)}
.header-nav{top:35px;left:0}
.hero{position:absolute;left:0;top:70px;width:956px;height:340px}
.hero-media{position:absolute;inset:0;background:linear-gradient(100deg,#0c0c0f 0%,#17181c 35%,#243f48 52%,#2f5560 62%,#4d4f57 78%,#5b5d66 100%)}
.hero-copy{position:absolute;left:86px;top:120px;width:284px}
.hero-kicker{font-size:18px;font-weight:700}
.hero-title{font-size:35px;font-weight:700;margin-top:14px;letter-spacing:.5px}
.hero-text{font-size:13px;line-height:19px;text-align:justify;margin-top:12px;margin-left:3px}
.btn{display:flex;align-items:center;justify-content:center;background:var(--button);color:var(--ink);border-radius:8px;font-family:"Playfair Display",serif;font-weight:600;text-decoration:none;box-shadow:0 2px 6px rgba(0,0,0,.35)}
.hero-btn{position:absolute;left:93px;top:302px;width:129px;height:37px;font-size:16px}
.dots-band{position:absolute;left:0;top:410px;width:956px;height:26px;background:linear-gradient(180deg,#0b0c11,#161a26);box-shadow:0 3px 6px rgba(0,0,0,.4)}
.dots{position:absolute;left:400px;top:6px;display:flex;gap:12px}
.dot{width:12px;height:12px;border-radius:50%;background:var(--ink)}
.dot.is-off{background:var(--dot-off)}
.section-title{position:absolute;left:90px;top:502px;font-size:33px;font-weight:700}
.slider-arrows{position:absolute;left:802px;top:551px;display:flex;gap:6px}
.arrow{width:28px;height:28px;border-radius:50%;background:var(--ink);display:flex;align-items:center;justify-content:center}
.arrow svg{width:12px;height:12px;stroke:#1b1e29;stroke-width:2.5;fill:none}
.card{position:absolute;top:605px;width:299px;height:254px;background:var(--slate-light);box-shadow:0 2px 8px rgba(0,0,0,.35)}
.cover{position:absolute;left:18px;top:13px;width:122px;height:228px;background:linear-gradient(90deg,#b7bfd0 0%,#6e7690 45%,#c81e1e 60%,#e8e8e8 75%,#cfcfcf 100%)}
.card-title{position:absolute;left:169px;top:29px;font-size:17px;font-weight:700}
.card-text{position:absolute;left:169px;top:57px;width:118px;font-size:11px;line-height:19px}
.card-actions{position:absolute;left:169px;top:151px;display:flex;gap:21px}
.card-actions svg{width:21px;height:21px;fill:var(--ink)}
.card-btn{position:absolute;left:156px;top:192px;width:130px;height:37px;font-size:16px}
.site-footer{position:absolute;left:0;top:935px;width:956px;height:265px;background:var(--night)}
.site-footer .brand{left:50%;transform:translateX(-50%);top:44px}
.footer-nav{top:133px;left:0}
.socials{position:absolute;top:171px;left:406px;display:flex;gap:41px}
.social{width:21px;height:21px;border-radius:3px;background:var(--ink)}
.copyright{position:absolute;top:223px;width:100%;text-align:center;font-size:14px}
</style>
</head>
<body>
<header class="site-header">
  <div class="brand"><span class="brand-dot"></span><span class="brand-name">Talemoor</span></div>
  <nav class="nav header-nav">
    <a class="nav-item" style="left:304px;top:-10px"><svg viewBox="0 0 20 20"><circle cx="10" cy="10" r="9"/><rect x="9" y="8" width="2" height="7" fill="#1c2030"/><circle cx="10" cy="5.5" r="1.3" fill="#1c2030"/></svg>About</a>
    <a class="nav-item" style="left:407px;top:-10px"><svg viewBox="0 0 20 20"><circle cx="8" cy="8" r="6" fill="none" stroke="#fff" stroke-width="2.5"/><rect x="12" y="13" width="3" height="7" transform="rotate(-45 13 14)"/></svg>True Crime</a>
    <a class="nav-item" style="left:547px;top:-10px"><svg viewBox="0 0 20 20"><circle cx="10" cy="10" r="8" fill="none" stroke="#fff" stroke-width="2"/><path d="M2 10h16M10 2v16" stroke="#fff" stroke-width="1.5"/></svg>Sport</a>
    <a class="nav-item" style="left:666px;top:-10px"><svg viewBox="0 0 20 20"><rect x="7" y="2" width="2" height="13"/><circle cx="5.5" cy="15" r="3"/><path d="M9 2l7 2v3l-7-2z"/></svg>Music</a>
    <a class="nav-item" style="left:778px;top:-10px"><svg viewBox="0 0 24 20" style="width:24px"><path d="M1 3c4-1 8-1 10 1v15c-2-2-6-2-10-1zM23 3c-4-1-8-1-10 1v15c2-2 6-2 10-1z"/></svg>Authors</a>
  </nav>
</header>

<section class="hero">
  <div class="hero-media" role="img" aria-label="Photo of headphones resting on a teal book beside a plant on a dark desk"></div>
  <div class="hero-copy">
    <p class="hero-kicker serif">Welcome To</p>
    <h1 class="hero-title serif">TALEMOOR</h1>
    <p class="hero-text">Lorem ipsum dolor sit amet, consectetur adipiscing elit, sed do eiusmod tempor incididunt ut labore.</p>
  </div>
  <a class="btn hero-btn">Get Started</a>
</section>

<div class="dots-band">
  <div class="dots"><span class="dot"></span><span class="dot"></span><span class="dot is-off"></span><span class="dot"></span><span class="dot"></span><span class="dot"></span><span class="dot"></span></div>
</div>

<h2 class="section-title serif">Recommonded For You</h2>
<div class="slider-arrows">
  <span class="arrow"><svg viewBox="0 0 12 12"><path d="M8 1L3 6l5 5"/></svg></span>
  <span class="arrow"><svg viewBox="0 0 12 12"><path d="M4 1l5 5-5 5"/></svg></span>
</div>

<article class="card" style="left:13px">
  <div class="cover" role="img" aria-label="Book cover artwork"></div>
  <h3 class="card-title serif">Lorum ipsum</h3>
  <p class="card-text">Lorem ipsum dolor sit amet, consectetur adipiscing elit, sed do eiusmod.</p>
  <div class="card-actions">
    <svg viewBox="0 0 24 24"><path d="M12 21l-9-9a5 5 0 0 1 9-6 5 5 0 0 1 9 6z"/></svg>
    <svg viewBox="0 0 24 24"><circle cx="12" cy="12" r="11"/><path d="M12 5v10M7 11l5 5 5-5M7 19h10" stroke="#323950" stroke-width="2.2" fill="none"/></svg>
    <svg viewBox="0 0 24 24"><path d="M12 2c6 0 11 4 11 9.5S18 21 12 21c-1.5 0-3-.3-4-.7L2 22l2-5c-1-1.6-2-3.5-2-5.5C2 6 6 2 12 2z"/></svg>
  </div>
  <a class="btn card-btn">Buy Now</a>
</article>
<article class="card" style="left:330px">
  <div class="cover" role="img" aria-label="Book cover artwork"></div>
  <h3 class="card-title serif">Lorum ipsum</h3>
  <p class="card-text">Lorem ipsum dolor sit amet, consectetur adipiscing elit, sed do eiusmod.</p>
  <div class="card-actions">
    <svg viewBox="0 0 24 24"><path d="M12 21l-9-9a5 5 0 0 1 9-6 5 5 0 0 1 9 6z"/></svg>
    <svg viewBox="0 0 24 24"><circle cx="12" cy="12" r="11"/><path d="M12 5v10M7 11l5 5 5-5M7 19h10" stroke="#323950" stroke-width="2.2" fill="none"/></svg>
    <svg viewBox="0 0 24 24"><path d="M12 2c6 0 11 4 11 9.5S18 21 12 21c-1.5 0-3-.3-4-.7L2 22l2-5c-1-1.6-2-3.5-2-5.5C2 6 6 2 12 2z"/></svg>
  </div>
  <a class="btn card-btn">Buy Now</a>
</article>
<article class="card" style="left:648px">
  <div class="cover" role="img" aria-label="Book cover artwork"></div>
  <h3 class="card-title serif">Lorum ipsum</h3>
  <p class="card-text">Lorem ipsum dolor sit amet, consectetur adipiscing elit, sed do eiusmod.</p>
  <div class="card-actions">
    <svg viewBox="0 0 24 24"><path d="M12 21l-9-9a5 5 0 0 1 9-6 5 5 0 0 1 9 6z"/></svg>
    <svg viewBox="0 0 24 24"><circle cx="12" cy="12" r="11"/><path d="M12 5v10M7 11l5 5 5-5M7 19h10" stroke="#323950" stroke-width="2.2" fill="none"/></svg>
    <svg viewBox="0 0 24 24"><path d="M12 2c6 0 11 4 11 9.5S18 21 12 21c-1.5 0-3-.3-4-.7L2 22l2-5c-1-1.6-2-3.5-2-5.5C2 6 6 2 12 2z"/></svg>
  </div>
  <a class="btn card-btn">Buy Now</a>
</article>

<footer class="site-footer">
  <div class="brand"><span class="brand-dot"></span><span class="brand-name">Talemoor</span></div>
  <nav class="nav footer-nav">
    <a class="nav-item" style="left:196px;top:-10px"><svg viewBox="0 0 20 20"><circle cx="10" cy="10" r="9"/><rect x="9" y="8" width="2" height="7" fill="#0b0c11"/><circle cx="10" cy="5.5" r="1.3" fill="#0b0c11"/></svg>About</a>
    <a class="nav-item" style="left:299px;top:-10px"><svg viewBox="0 0 20 20"><circle cx="8" cy="8" r="6" fill="none" stroke="#fff" stroke-width="2.5"/><rect x="12" y="13" width="3" height="7" transform="rotate(-45 13 14)"/></svg>True Crime</a>
    <a class="nav-item" style="left:439px;top:-10px"><svg viewBox="0 0 20 20"><circle cx="10" cy="10" r="8" fill="none" stroke="#fff" stroke-width="2"/><path d="M2 10h16M10 2v16" stroke="#fff" stroke-width="1.5"/></svg>Sport</a>
    <a class="nav-item" style="left:558px;top:-10px"><svg viewBox="0 0 20 20"><rect x="7" y="2" width="2" height="13"/><circle cx="5.5" cy="15" r="3"/><path d="M9 2l7 2v3l-7-2z"/></svg>Music</a>
    <a class="nav-item" style="left:670px;top:-10px"><svg viewBox="0 0 24 20" style="width:24px"><path d="M1 3c4-1 8-1 10 1v15c-2-2-6-2-10-1zM23 3c-4-1-8-1-10 1v15c2-2 6-2 10-1z"/></svg>Authors</a>
  </nav>
  <div class="socials">
    <span class="social" role="img" aria-label="Social link"></span>
    <span class="social" role="img" aria-label="Social link"></span>
    <span class="social" role="img" aria-label="Social link"></span>
  </div>
  <p class="copyright">Copyright 2023 - TALEMOOR - All Rights Reserved</p>
</footer>
</body>
</html>
```